Holistic/ Sports Psychologist needs flyer design

I need a flyer designed that catches the attention of potential customers - (parents of young athletes and athletes) who may be looking for psychological services. I have a logo and all the relevant info for the flyer but would like someone to take it and make it look creative, fun, fresh and attention getting for high school and college athletes. The colors used can be from my logo design which represents my holistic approach.
Target Market(s)
high school and collegiate athletes
Industry/Entity Type
sports psychology
Requirements
Must have
- Info I put on the flyer with my logo and please add some graphics and color based on my logo

```html
<!DOCTYPE html>
<html lang="en">
<head>
<meta charset="utf-8">
<title>Dr. Elaine Hartwell – Holistic Psychology Flyer</title>
<link href="https://fonts.googleapis.com/css2?family=Lexend:wght@500;600;700;800&family=Outfit:wght@400;500;600;700&display=swap" rel="stylesheet">
<style>
  :root {
    --blue: #35679c;
    --green: #a8d175;
    --green-pale: #d5e9bc;
    --band: #e8f0f7;
    --ink: #2b2b2b;
    --white: #ffffff;
  }
  * { margin: 0; padding: 0; box-sizing: border-box; }
  html, body { width: 849px; height: 1200px; overflow: hidden; background: var(--white); }
  body { font-family: "Outfit", sans-serif; color: var(--ink); }
  .flyer { position: relative; width: 849px; height: 1200px; overflow: hidden; }
  .backdrop { position: absolute; inset: 0; }
  .abs { position: absolute; }
  .nowrap { white-space: nowrap; }

  .brand-mark { left: 70px; top: 58px; width: 140px; height: 140px; border-radius: 50%; background: var(--blue); }
  .brand-bar { left: 209px; top: 139px; width: 437px; height: 32px; background: var(--green); }
  .brand-name { left: 228px; top: 88px; font-family: "Outfit", sans-serif; font-weight: 500; font-size: 40px; color: var(--blue); letter-spacing: 1px; }

  .telehealth-icon { left: 452px; top: 217px; width: 104px; height: 86px; }
  .telehealth-text { left: 564px; top: 217px; }
  .telehealth-text .lead { font-size: 20px; line-height: 16px; font-weight: 400; color: var(--ink); }
  .telehealth-text .word { font-family: "Lexend", sans-serif; font-weight: 800; font-size: 44px; line-height: 52px; letter-spacing: -1px; color: var(--ink); }

  .sessions { right: 115px; top: 334px; text-align: right; line-height: 20px; }
  .sessions .lead { font-size: 18px; }
  .sessions .time { font-family: "Lexend", sans-serif; font-weight: 700; font-size: 18px; }
  .clock-icon { left: 742px; top: 324px; width: 44px; height: 52px; }

  .headline { left: 68px; top: 318px; font-family: "Lexend", sans-serif; font-weight: 800; color: var(--blue); }
  .headline .line { display: block; font-size: 68px; line-height: 60px; letter-spacing: -2.5px; }
  .subline { left: 71px; top: 452px; font-family: "Lexend", sans-serif; font-weight: 700; font-size: 32px; letter-spacing: -0.8px; color: var(--blue); }

  .section-title { left: 71px; top: 528px; font-family: "Lexend", sans-serif; font-weight: 700; font-size: 25px; line-height: 29px; letter-spacing: -0.7px; color: var(--ink); white-space: nowrap; }

  .benefits { left: 71px; top: 605px; width: 720px; list-style: none; }
  .benefits li { position: relative; padding-left: 19px; margin-bottom: 10px; }
  .benefits li::before { content: ""; position: absolute; left: 2px; top: 3px; width: 4px; height: 12px; background: var(--blue); transform: skewX(-40deg); }
  .benefits h3 { font-family: "Outfit", sans-serif; font-weight: 700; font-size: 15px; line-height: 17px; color: var(--ink); text-transform: uppercase; }
  .benefits p { font-size: 14.2px; line-height: 15px; }

  .tag { left: 72px; top: 885px; width: 193px; height: 34px; background: var(--blue); overflow: hidden; }
  .tag::before { content: ""; position: absolute; left: -20px; top: 0; width: 56px; height: 34px; background: var(--green); transform: skewX(-28deg); }
  .tag span { position: absolute; left: 47px; top: 1px; font-family: "Lexend", sans-serif; font-weight: 700; font-size: 22px; color: var(--white); }

  .bio { left: 72px; top: 932px; font-size: 14.2px; line-height: 15px; white-space: nowrap; }
  .bio strong { font-weight: 700; }
  .specialties { left: 72px; top: 1008px; font-size: 14.2px; line-height: 15px; white-space: nowrap; }

  .address { left: 69px; top: 1114px; font-family: "Lexend", sans-serif; font-weight: 700; font-size: 18px; line-height: 21px; color: var(--white); letter-spacing: -0.3px; font-style: normal; }
  .website { right: 70px; top: 1101px; font-size: 14px; letter-spacing: 3px; color: var(--white); }
  .phone { right: 70px; top: 1124px; font-family: "Lexend", sans-serif; font-weight: 800; font-size: 30px; color: var(--white); letter-spacing: -0.5px; }
  .phone-icon { left: 536px; top: 1128px; width: 17px; height: 28px; }
</style>
</head>
<body>
<main class="flyer">
  <svg class="backdrop" width="849" height="1200" viewBox="0 0 849 1200" aria-hidden="true">
    <circle cx="670" cy="-20" r="86" fill="var(--green-pale)"/>
    <path d="M700 0 H849 V128 C790 130 735 95 735 40 Z" fill="var(--green-pale)"/>
    <rect x="0" y="507" width="849" height="693" fill="var(--band)"/>
    <path d="M0 1065 Q600 1090 849 960 V1200 H0 Z" fill="var(--green)"/>
    <path d="M0 1080 Q620 1105 849 1010 V1200 H0 Z" fill="var(--blue)"/>
  </svg>

  <div class="abs brand-mark" aria-hidden="true"></div>
  <div class="abs brand-bar"></div>
  <div class="abs brand-name">Dr. Elaine Hartwell</div>

  <svg class="abs telehealth-icon" viewBox="0 0 104 86" aria-hidden="true">
    <rect x="3" y="3" width="98" height="66" rx="5" fill="none" stroke="var(--ink)" stroke-width="5"/>
    <path d="M38 79 H66 M44 70 V79 M60 70 V79" stroke="var(--ink)" stroke-width="5"/>
    <path d="M52 56 C30 42 22 32 28 22 C34 12 46 14 52 22 C58 14 70 12 76 22 C82 32 74 42 52 56 Z" fill="none" stroke="var(--ink)" stroke-width="4"/>
    <path d="M22 36 H40 L45 26 L52 46 L58 34 H82" fill="none" stroke="var(--ink)" stroke-width="4" stroke-linejoin="round"/>
  </svg>
  <div class="abs telehealth-text">
    <div class="lead">All services are provided<br>online via</div>
    <div class="word">telehealth</div>
  </div>

  <div class="abs sessions">
    <div class="lead">Sessions are</div>
    <div class="time">30 or 55 minutes</div>
  </div>
  <svg class="abs clock-icon" viewBox="0 0 44 52" aria-hidden="true">
    <rect x="16" y="2" width="12" height="5" fill="var(--ink)"/>
    <rect x="20" y="6" width="4" height="6" fill="var(--ink)"/>
    <circle cx="22" cy="31" r="18" fill="none" stroke="var(--ink)" stroke-width="5"/>
    <path d="M22 31 V19 A12 12 0 1 1 11 36 Z" fill="var(--ink)"/>
  </svg>

  <h1 class="abs headline"><span class="line">Holistic</span><span class="line">Psychology</span></h1>
  <p class="abs subline">and sports Psychology Consulting</p>

  <h2 class="abs section-title">Ways to Improve Athletic Performance Using Sports and<br>Holistic Psychology</h2>

  <ul class="abs benefits">
    <li><h3>Mental Skills Training</h3><p>Ex: visualization, goal-setting, motivation, self- talk, mindset, concentration techniques.</p></li>
    <li><h3>Performance&nbsp; Enhancement</h3><p>Eliminate psychological barriers that are hindering performance such as self- doubt, perfectionism, fear of failure, and burnout.</p></li>
    <li><h3>Mental Health</h3><p>Anxiety and stress management by using relaxation techniques, breathwork, and mindfulness practices.</p></li>
    <li><h3>Injury Recovery Support</h3><p>Assist athletes in maintaining resilience and positive mental attitude during rehabilitation as well as processing emotions relating to any potential trauma caused by the injury or life transitions resulting from it.</p></li>
    <li><h3>Burnout Prevention</h3><p>Teach athletes how to have balance in sports and life so they can experience longevity in their sports as well as overall optimal health and well-being.</p></li>
  </ul>

  <div class="abs tag"><span>Background</span></div>
  <p class="abs bio"><strong>Dr. Elaine Hartwell</strong> is a licensed psychologist. She understands the unique experiences of athletes due<br>to her background as an All-American swimmer, collegiate and age group swim coach, parent of a<br>collegiate/professional athlete, and sports psychology researcher. She works with athletes to<br>optimize performance and overall well-being.</p>
  <p class="abs specialties">Her specializations include: performance anxiety, mental performance, stress<br>management, anxiety, depressions, trauma, life transitions,<br>relationship issues, injury, and sleep.</p>

  <address class="abs address">2280 Harbor View Lane #104<br>Seabrook Point, FL 32990</address>
  <div class="abs website">drelainehartwell.com</div>
  <svg class="abs phone-icon" viewBox="0 0 17 28" aria-hidden="true">
    <rect x="1.5" y="1.5" width="14" height="25" rx="3" fill="none" stroke="var(--green)" stroke-width="2"/>
    <path d="M6 23 H11" stroke="var(--green)" stroke-width="2"/>
  </svg>
  <div class="abs phone">555-318-4270</div>
</main>
</body>
</html>
```